Initial website for sport tech startup

We are currently in the R&D phases of our new product. It’s a headband to prevent concussion in the soccer market initially.

We have 2 products, one that’s basic aimed at the youth market and the other more technology driven that’s aimed at the academies and professional market.

Initially the product will launch in the UK

Target Market(s)

Youth soccer players and parents in UK, Soccer Clubs, Federations.

Industry/Entity Type

Sporting Good

Coding

Coded - Design and coding required

Number of Pages Required

5+ page

Requirements
Must have
• Professional style that can be adapted and changed over the coming months.
Nice to have
• Ecommerce ability in the future.

```html
<!DOCTYPE html>
<html lang="en">
<head>
<meta charset="utf-8">
<title>HELMORA – Making Sport Safer</title>
<link rel="stylesheet" href="https://fonts.googleapis.com/css2?family=Cantarell:wght@400;700&family=Nunito+Sans:wght@300;400&display=swap">
<style>
:root{
  --ink:#1f1d1e;
  --bar:#231f20;
  --nav-active:#5b5c5f;
  --band:#a7a9ad;
  --blue:#2a8fdc;
  --blue-text:#2b96e0;
  --white:#ffffff;
  --card-line:#3a3a3a;
  --icon:#1f1d1e;
}
*{box-sizing:border-box;margin:0;padding:0}
html,body{width:1200px;height:2700px;overflow:hidden;background:var(--white)}
body{position:relative;font-family:"Nunito Sans",Arial,sans-serif;color:var(--ink)}
.display{font-family:"Cantarell",Arial,sans-serif}

/* header */
.site-header{position:absolute;left:0;top:0;width:1200px;height:90px;background:var(--bar)}
.brand{position:absolute;left:24px;top:18px;height:56px;display:flex;align-items:center;gap:12px}
.brand-mark{width:14px;height:14px;background:var(--blue)}
.brand-name{font-family:"Cantarell",Arial,sans-serif;font-size:42px;color:var(--white);letter-spacing:1px;line-height:1}
.main-nav{position:absolute;right:40px;top:0;height:90px;display:flex}
.main-nav a{display:flex;align-items:center;padding:0 9px;color:var(--white);text-decoration:none;font-family:"Cantarell",Arial,sans-serif;font-size:26px}
.main-nav a.is-current{background:var(--nav-active)}

/* hero */
.hero{position:absolute;left:0;top:90px;width:1200px;height:585px;background:linear-gradient(160deg,#2c2e2b 0%,#1e201d 45%,#3a3530 70%,#242622 100%)}
.hero-title{position:absolute;left:0;top:330px;width:1200px;text-align:center;color:var(--white);font-size:76px;font-weight:400;letter-spacing:1px}

/* products */
.section-title{position:absolute;left:0;width:1200px;text-align:center;font-size:56px;font-weight:400;color:var(--ink)}
.products-title{top:688px}
.product-card{position:absolute;width:398px;height:550px;border:1.5px solid var(--card-line);border-radius:26px;background:var(--white);box-shadow:6px 8px 8px rgba(0,0,0,.45)}
.product-card.v1{left:153px;top:773px}
.product-card.v2{left:643px;top:769px}
.product-name{text-align:center;font-size:44px;font-weight:400;margin-top:12px;line-height:1.1}
.product-sub{text-align:center;font-family:"Cantarell",Arial,sans-serif;font-size:28px;line-height:1;margin-top:-4px}
.product-image{position:absolute;left:85px;top:78px;width:235px;height:140px;border-radius:30px 30px 60px 20px}
.v1 .product-image{background:linear-gradient(135deg,#5c6570,#3c434b)}
.v2 .product-image{top:100px;left:100px;width:200px;height:120px;background:linear-gradient(135deg,#ff7087,#f04863)}
.product-copy{position:absolute;left:27px;top:242px;width:350px;font-size:15.5px;line-height:21px;font-weight:300}
.v2 .product-copy{top:237px}
.feature-icons{position:absolute;left:90px;top:405px;display:flex;gap:22px}
.feature-icons svg{width:36px;height:36px;fill:none;stroke:var(--icon);stroke-width:1.8;stroke-linecap:round;stroke-linejoin:round}
.product-cta{position:absolute;left:65px;top:474px;width:266px;height:56px;background:var(--blue);color:var(--white);border-radius:4px;display:flex;align-items:center;justify-content:center;font-family:"Cantarell",Arial,sans-serif;font-size:30px}

/* about band */
.about-band{position:absolute;left:0;top:1349px;width:1200px;height:675px;background:var(--band)}
.about-block{position:absolute;left:74px;width:1060px;color:var(--white)}
.mission{top:80px}
.market{top:363px}
.about-head{display:flex;align-items:center;gap:14px}
.about-head svg{width:62px;height:62px;fill:none;stroke:var(--white);stroke-width:2.4;stroke-linecap:round;stroke-linejoin:round}
.about-head h2{font-size:56px;font-weight:400}
.about-copy{margin-left:89px;margin-top:10px;font-size:23.5px;line-height:31px;font-weight:300;width:970px}

/* team */
.team-title{top:2040px}
.team-member{position:absolute;top:2108px;width:300px;text-align:center}
.team-member.one{left:132px}
.team-member.two{left:449px}
.team-member.three{left:767px}
.portrait{width:154px;height:154px;border-radius:50%;margin:0 auto 6px}
.one .portrait{background:linear-gradient(135deg,#c8262c,#e9d6cf)}
.two .portrait{background:linear-gradient(135deg,#e9ecef,#1d3a75)}
.three .portrait{background:linear-gradient(135deg,#dfe7ee,#8fa2b5)}
.member-name{font-family:"Cantarell",Arial,sans-serif;font-size:24px;font-weight:400;line-height:28px}
.member-role{font-family:"Cantarell",Arial,sans-serif;font-size:21px;color:var(--blue-text);line-height:24px}
.member-bio{font-size:14.5px;line-height:18.5px;font-weight:400;margin-top:3px}
.advisory{position:absolute;left:46px;top:2487px;width:1120px;display:flex;gap:6px}
.advisory-label{font-family:"Cantarell",Arial,sans-serif;font-size:24px;color:var(--blue-text);white-space:nowrap;padding-top:2px}
.advisory-copy{font-size:16.5px;line-height:19px}

/* footer */
.site-footer{position:absolute;left:0;top:2572px;width:1200px;height:128px;background:var(--bar);color:var(--white)}
.footer-brand{position:absolute;left:105px;top:44px;display:flex;align-items:center;font-family:"Cantarell",Arial,sans-serif;font-size:25px}
.footer-brand .divider{width:4px;height:42px;background:var(--blue);margin:0 12px}
.footer-contact{position:absolute;left:860px;top:22px;font-family:"Cantarell",Arial,sans-serif;font-size:26px;line-height:42px}
.footer-contact div{display:flex;align-items:center;gap:6px}
.footer-contact svg{width:32px;height:30px;fill:var(--white)}
</style>
</head>
<body>

<header class="site-header">
  <div class="brand"><span class="brand-name">HELMORA</span><span class="brand-mark"></span></div>
  <nav class="main-nav">
    <a href="#products">PRODUCTS</a>
    <a href="#about" class="is-current">ABOUT US</a>
    <a href="#login">LOGIN</a>
  </nav>
</header>

<section class="hero" role="img" aria-label="Photograph of two footballers' legs challenging for a ball on an artificial pitch, darkened">
  <h1 class="hero-title display">MAKING SPORT SAFER</h1>
</section>

<h2 class="section-title products-title display" id="products">Our Products</h2>

<article class="product-card v1">
  <h3 class="product-name display">V1 Headband</h3>
  <div class="product-image" role="img" aria-label="Illustration of the grey V1 protective headband"></div>
  <p class="product-copy">Now represents the opportunity to develop a head protection product for use in contact sports to help reduce the impact of concussion and product a fool proof way of measuring temperature in a post pandemic world, accepting that there is no such thing as concussion-proof head protection.</p>
  <div class="feature-icons">
    <svg viewBox="0 0 36 36"><path d="M18 3l12 5v9c0 8-5 13-12 16C11 30 6 25 6 17V8z"/><circle cx="18" cy="18" r="7"/><path d="M15 18l2.5 2.5L21.5 16"/></svg>
    <svg viewBox="0 0 36 36"><path d="M18 4C14 11 9 17 9 23a9 9 0 0018 0c0-6-5-12-9-19z"/></svg>
    <svg viewBox="0 0 36 36"><path d="M30 4C18 6 9 14 9 26l1 2c12 0 19-9 20-24z"/><path d="M5 32L22 13"/></svg>
    <svg viewBox="0 0 36 36"><circle cx="13" cy="22" r="4"/><path d="M13 13v3M13 28v3M4 22h3M19 22h3M7 16l2 2M17 26l2 2M7 28l2-2M17 18l2-2"/><circle cx="25" cy="11" r="3"/><path d="M25 4v2M25 16v2M18 11h2M30 11h2"/></svg>
  </div>
  <div class="product-cta">BUY NOW!</div>
</article>

<article class="product-card v2">
  <h3 class="product-name display">V2 Headband</h3>
  <p class="product-sub">with Tracker!</p>
  <div class="product-image" role="img" aria-label="Illustration of the pink V2 headband with tracker"></div>
  <p class="product-copy">Now represents the opportunity to develop a head protection product for use in contact sports to help reduce the impact of concussion and product a fool proof way of measuring temperature in a post pandemic world, accepting that there is no such thing as concussion-proof head protection.</p>
  <div class="feature-icons">
    <svg viewBox="0 0 36 36"><path d="M18 3l12 5v9c0 8-5 13-12 16C11 30 6 25 6 17V8z"/><circle cx="18" cy="18" r="7"/><path d="M15 18l2.5 2.5L21.5 16"/></svg>
    <svg viewBox="0 0 36 36"><path d="M18 4C14 11 9 17 9 23a9 9 0 0018 0c0-6-5-12-9-19z"/></svg>
    <svg viewBox="0 0 36 36"><path d="M30 4C18 6 9 14 9 26l1 2c12 0 19-9 20-24z"/><path d="M5 32L22 13"/></svg>
    <svg viewBox="0 0 36 36"><circle cx="13" cy="22" r="4"/><path d="M13 13v3M13 28v3M4 22h3M19 22h3M7 16l2 2M17 26l2 2M7 28l2-2M17 18l2-2"/><circle cx="25" cy="11" r="3"/><path d="M25 4v2M25 16v2M18 11h2M30 11h2"/></svg>
  </div>
  <div class="product-cta">COMING SOON!</div>
</article>

<section class="about-band" id="about">
  <div class="about-block mission">
    <div class="about-head">
      <svg viewBox="0 0 62 62"><circle cx="26" cy="36" r="22"/><circle cx="26" cy="36" r="14"/><circle cx="26" cy="36" r="6"/><path d="M26 36L52 10M46 6l1 9 9 1M52 10l4-4"/></svg>
      <h2 class="display">Our Mission</h2>
    </div>
    <p class="about-copy">Helmora is designing and developing head protection. Helmora is designing and developing head protection products to reduce the likelihood of concussion when playing sports. Exploring and understanding medical insights, material science and composites research, current and former players experiences and governing bodies guidelines has allowed Helmora to develop the safety, style, form and function requirements of a suitable product</p>
  </div>
  <div class="about-block market">
    <div class="about-head">
      <svg viewBox="0 0 62 62"><path d="M2 58h58M6 58V48h8v10M18 58V40h8v18M30 58V30h8v28M44 58V12M38 18l6-8 6 8M50 58V18"/></svg>
      <h2 class="display">Market &amp; Demand</h2>
    </div>
    <p class="about-copy">Soccer has no head protection product despite recent high. Soccer has no head protection product despite recent high profile head injuries, concern over the long term damage of heading the ball and greater damage of concussion in women. There are in excess of 11m people actively playing football in the UK alone (8m men, 3m women). There is no product that exists for netball, field hockey and lacrosse, as further example of the market</p>
  </div>
</section>

<h2 class="section-title team-title display">Our Team</h2>

<div class="team-member one">
  <div class="portrait" role="img" aria-label="Portrait photo of Martin Calloway"></div>
  <p class="member-name">Martin Calloway</p>
  <p class="member-role">Founder &amp; CEO</p>
  <p class="member-bio">Martin has a wealth of experience of growing start-ups and exiting businesses, from professional services to technology companies, in recent years Martin has been an executive advisor to many global sporting talents, football clubs, right holders and other sports companies.</p>
</div>

<div class="team-member two">
  <div class="portrait" role="img" aria-label="Portrait photo of Helen Farrow"></div>
  <p class="member-name">Helen Farrow</p>
  <p class="member-role">Co-Founder &amp; COO</p>
  <p class="member-bio">Helen has been planning and delivering commercial, large scale transformation projects within people based, high-profile and global environments for the last 15 years. COO to a former UK Prime Minister, transforming his business globally across 30 legal jurisdiction</p>
</div>

<div class="team-member three">
  <div class="portrait" role="img" aria-label="Portrait photo of Graham Tate"></div>
  <p class="member-name">Graham Tate</p>
  <p class="member-role">CCO</p>
  <p class="member-bio">Graham started his career in retail banking, later experience in corporate and private banking. Since leaving the corporate world in 2007, Graham has been bringing people and companies together in enable funding and development of projects across Europe.</p>
</div>

<div class="advisory">
  <span class="advisory-label">Advisory Board:</span>
  <p class="advisory-copy">Our initial advisory board is headed by the former chairman of the National Players Union and chairman of the Grassroots Players Guild (3m members), Mr Peter Ashdown. Peter is working with us to liaise with clubs, former players and federations across UK sport.</p>
</div>

<footer class="site-footer">
  <div class="footer-brand">HELMORA LTD<span class="divider"></span>Making Sport Safer</div>
  <div class="footer-contact">
    <div><svg viewBox="0 0 32 30"><path d="M7 2l5 6-3 4c2 4 5 7 9 9l4-3 6 5-3 5C14 27 4 17 3 6z"/></svg>+44 208 5550142</div>
    <div><svg viewBox="0 0 32 30"><path d="M2 6h28v19H2z M4 8l12 9 12-9" fill="none" stroke="#fff" stroke-width="2.5"/></svg>info@helmora.co.uk</div>
  </div>
</footer>

</body>
</html>
```